Anzeigengestaltung Serviceblock
Sehr serviceorientiert, zügig und kreativ!
Zielgruppe
Wir sind eine klassische Steuerberatungsgesellschaft und richten uns vor allem an mittelständische Unternehmen und an das Handwerk. Zu finden sind wir unter www.fiskoralo.de.
Aufgabenstellung
Wir beabsichtigen eine regelmäßige monatliche Werbung mittels eines Serviceblocks in regionalen Zeitungen. Dazu wollen wir eine Art Rahmendesign, dass immer gleich aussieht, von uns aber mit wechselnden Info- Texten gefüllt werden kann. Das Design soll an das Design unserer Homepage angelehnt sein und unser Logo umfassen. Zudem sollen unsere Kontaktdaten gut zu ersehen sein. Muster solcher Serviceblöcke laden wir hoch - die sind aber nicht unbedingt unser Geschmack. Das Maß der Anzeige soll 325 mm breit und 163 mm hoch sein. Wir benötigen das Design als pdf, jpg und sonstiges zeitungskompatibles Format.

```html
<!DOCTYPE html>
<html lang="de">
<head>
<meta charset="utf-8">
<title>Fiskoralo – Serviceblock</title>
<link rel="stylesheet" href="https://fonts.googleapis.com/css2?family=Montserrat:wght@700&family=Open+Sans:wght@400;600;700&display=swap">
<style>
  :root {
    --teal: #137b87;
    --teal-deep: #0f6f7a;
    --teal-dark: #0d6671;
    --photo-mid: #5d8f9a;
    --photo-light: #a9bcc0;
    --white: #ffffff;
    --paper: #eeeeee;
    --frame: #7d8f93;
    --page: #e6e8e9;
  }
  * { box-sizing: border-box; margin: 0; padding: 0; }
  html, body { width: 1200px; height: 700px; overflow: hidden; background: var(--page); }
  body { font-family: "Open Sans", Arial, sans-serif; color: var(--white); }

  .ad {
    position: absolute; left: 30px; top: 63px;
    width: 1140px; height: 574px;
    background: var(--teal); overflow: hidden;
  }
  .ad__photo {
    position: absolute; left: 520px; top: 130px; width: 620px; height: 350px;
    background: linear-gradient(100deg, var(--teal) 0%, var(--photo-mid) 40%, var(--photo-light) 75%, #c7c9c4 100%);
  }
  .ad__headline {
    position: absolute; left: 40px; top: 34px;
    font-family: "Montserrat", Arial, sans-serif; font-weight: 700;
    font-size: 40px; line-height: 1.15; letter-spacing: 0.5px;
  }
  .ad__rule { position: absolute; left: 42px; top: 140px; width: 72px; height: 4px; background: var(--white); }

  .ad__column {
    position: absolute; width: 300px;
    font-size: 12.5px; line-height: 1.45;
  }
  .ad__column p + p { margin-top: 10px; }
  .ad__column--one { left: 42px; top: 166px; }
  .ad__column--two { left: 366px; top: 196px; }
  .ad__column--three { left: 690px; top: 226px; }

  .ad__logo-box {
    position: absolute; left: 0; top: 430px; width: 270px; height: 144px;
    background: var(--paper); padding: 18px;
  }
  .ad__logo-frame {
    width: 100%; height: 100%; border: 2px solid var(--frame);
    display: flex; align-items: center; justify-content: center; gap: 12px;
  }
  .ad__logo-dot { width: 30px; height: 30px; border-radius: 50%; background: var(--teal); }
  .ad__logo-name { font-weight: 700; font-size: 26px; color: var(--teal); letter-spacing: 1px; }

  .ad__caption {
    position: absolute; left: 270px; top: 480px; width: 560px; height: 94px;
    background: var(--teal-deep); padding: 14px 22px;
    font-size: 14.5px; line-height: 1.45;
  }
  .ad__caption strong { font-weight: 700; }

  .ad__contact { position: absolute; left: 830px; top: 470px; width: 310px; height: 104px; }
  .ad__phone {
    height: 60px; background: var(--white); color: var(--teal);
    display: flex; align-items: center; gap: 12px; padding-left: 24px;
    font-weight: 700; font-size: 25px;
  }
  .ad__phone svg { width: 26px; height: 26px; }
  .ad__url {
    height: 44px; background: var(--teal-dark);
    display: flex; align-items: center; justify-content: flex-end; padding-right: 24px;
    font-weight: 700; font-size: 19px;
  }
</style>
</head>
<body>
  <section class="ad">
    <div class="ad__photo" role="img" aria-label="Foto: Frau am Laptop an einem Holztisch, teal überlagert"></div>

    <h1 class="ad__headline">Are you looking for<br>Tax Consultant?</h1>
    <div class="ad__rule"></div>

    <div class="ad__column ad__column--one">
      <p>Lorem ipsum dolor sit amet, consectetur adipiscing elit. Integer commodo elit vehicula, dictum tortor ac, vestibulum eros. Lorem ipsum dolor sit amet, consectetur adipiscing elit. Donec tincidunt dolor id arcu vulputate gravida. Aliquam feugiat suscipit pulvinar. Praesent in interdum lectus. Praesent eget tortor eu eros tristique feugiat et a tortor. Ut consectetur, neque et venenatis molestie, arcu purus sodales urna, at tempor magna sem non elit. Duis augue sapien, convallis tristique volutpat et, luctus eu nibh. Maecenas auctor massa</p>
    </div>
    <div class="ad__column ad__column--two">
      <p>nec lacus sollicitudin, non tempor lectus lobortis. Etiam egestas ipsum vitae tortor vestibulum, in scelerisque quam elementum. Vestibulum ante ipsum primis in faucibus orci luctus et ultrices posuere cubilia curae; Ut tincidunt luctus tellus, a mattis nulla tempor in. Aliquam mattis faucibus lectus a vestibulum.</p>
      <p>Lorem ipsum dolor sit amet, consectetur adipiscing elit. In hac habitasse platea dictumst. Integer non pellentesque quam. Integer eget commodo elit. Ut blandit imperdiet aliquet. Phasellus eu tempor</p>
    </div>
    <div class="ad__column ad__column--three">
      <p>odio. Nunc auctor lorem bibendum, blandit ligula malesuada, lacinia purus. Etiam ac ex quis orci lobortis laoreet vel id risus. Etiam at nulla nec diam posuere consectetur. Ut sollicitudin lorem purus, in aliquet tellus congue non. Ut vel sapien ac turpis convallis euismod. Morbi elementum odio in lacus pellentesque varius. Aliquam nec ultrices dui, eu vestibulum ligula. Suspendisse tristique, quam nec mattis bibendum, eros elit consequat arcu, suscipit ultricies neque dui in velit. Ut convallis, velit a rhoncus</p>
    </div>

    <div class="ad__logo-box">
      <div class="ad__logo-frame">
        <span class="ad__logo-dot"></span>
        <span class="ad__logo-name">FISKORALO</span>
      </div>
    </div>

    <p class="ad__caption"><strong>FISKORALO</strong> betreut überwiegend klein- und mittelständische Unternehmen, Freie Berufe und Privatpersonen in allen Bereichen der Steuerberatung und betriebswirtschaftlichen Beratung.</p>

    <div class="ad__contact">
      <div class="ad__phone">
        <svg viewBox="0 0 24 24" aria-hidden="true"><path fill="currentColor" d="M6.6 10.8c1.4 2.8 3.8 5.1 6.6 6.6l2.2-2.2c.3-.3.7-.4 1-.2 1.1.4 2.3.6 3.6.6.6 0 1 .4 1 1V20c0 .6-.4 1-1 1C10.6 21 3 13.4 3 4c0-.6.4-1 1-1h3.5c.6 0 1 .4 1 1 0 1.3.2 2.5.6 3.6.1.3 0 .7-.2 1z"/><path fill="none" stroke="currentColor" stroke-width="1.6" stroke-linecap="round" d="M15 3.5a6 6 0 0 1 5.5 5.5M14.5 6.8a3 3 0 0 1 2.7 2.7"/></svg>
        <span>04431 5820714</span>
      </div>
      <div class="ad__url">www.fiskoralo.de</div>
    </div>
  </section>
</body>
</html>
```